Talvora Health Artificial Intelligence MedTech Software Website Refresh

We need a new website (old one at www.talvora-health.example is no longer relevant) for our medtech software company using artificial intelligence to deliver higher quality, faster and more cost effective care in oncology. The audiences are both healthcare providers and health insurance payers. We've created an extensive outline to follow and have the old site still live for easy content use and repurposing. Our primary need is a great overhaul to look and feel. If we find a successful designer, we will need additional work done for graphics and other presentation projects.

Target Market(s)

Health care providers (doctors) and administrators plus health insurers

Industry/Entity Type

Medtech

Number of Pages Required

5+ page

Font styles to use
Other font styles liked:
• Roboto see Style Guide

Requirements
Must have
• See attached brief
Nice to have
• See attached brief. We like www.carenix.example and www.plumotech.example as sites.
Should not have
• See attached brief

```html
<!DOCTYPE html>
<html lang="en">
<head>
<meta charset="utf-8">
<title>Talvora Health</title>
<link rel="stylesheet" href="https://fonts.googleapis.com/css2?family=Open+Sans:wght@400;600;700&family=Lato:wght@300;400;700&display=swap">
<style>
:root{
  --blue:#0f72bd;
  --nav-blue:#1f5fb0;
  --ink:#222;
  --text:#333;
  --orange-a:#ffd23f;
  --orange-b:#f9a12c;
  --line:#f5b531;
  --band:#f7f7f7;
  --ghost:#efefef;
  --field:#f3f3f3;
  --dark:#151515;
  --white:#fff;
}
*{margin:0;padding:0;box-sizing:border-box}
html,body{width:1200px;height:2821px;overflow:hidden;background:var(--white)}
body{position:relative;font-family:'Lato',sans-serif;color:var(--text)}
.abs{position:absolute}
.btn{position:absolute;border-radius:20px;background:linear-gradient(90deg,var(--orange-a),var(--orange-b));color:var(--white);font-size:12px;display:flex;align-items:center;justify-content:center;white-space:nowrap}

/* header */
.brand{left:0;top:0;width:263px;height:88px;background:var(--blue);clip-path:polygon(0 0,100% 0,91% 100%,0 100%)}
.brand-name{left:46px;top:28px;color:var(--white);font-family:'Open Sans',sans-serif;font-weight:700;font-size:22px;letter-spacing:.3px;white-space:nowrap}
.topline{left:263px;top:45px;width:937px;height:1px;background:#ccc}
.top-social{top:15px;width:12px;height:12px;border:1.5px solid #222;border-radius:2px}
.top-social.first{border-color:var(--orange-b)}
.top-sep{top:14px;width:1px;height:15px;background:#555}
.top-info{top:15px;font-size:10px;color:#222;white-space:nowrap}
.nav{top:60px;font-size:10px;color:#222;white-space:nowrap}
.nav.active{color:var(--nav-blue)}

/* hero */
.hero{left:0;top:88px;width:1200px;height:493px;background:linear-gradient(90deg,#7d7d7d 0%,#8f8f8f 40%,#7c7c7c 70%,#8b8b8b 100%)}
.hero-kicker{left:151px;top:234px;font-family:'Open Sans',sans-serif;font-size:37px;color:var(--white);font-weight:400;line-height:1.2;white-space:nowrap}
.hero-title{left:151px;top:278px;font-family:'Open Sans',sans-serif;font-size:46px;color:var(--white);font-weight:700;line-height:1.2;white-space:nowrap}
.hero-sub{left:151px;top:343px;font-size:16px;color:var(--white);line-height:1.2;white-space:nowrap}

/* about */
.about-photo{left:120px;top:690px;width:489px;height:366px;background:linear-gradient(120deg,#e9eef0,#cbd7dc 55%,#7fb9cf)}
.ghost{color:var(--ghost);font-family:'Open Sans',sans-serif;font-weight:700;white-space:nowrap;line-height:1}
.section-title{color:var(--blue);font-family:'Open Sans',sans-serif;font-weight:700;font-size:46px;line-height:1;white-space:nowrap}
.about-sub{left:640px;top:775px;font-family:'Open Sans',sans-serif;font-size:28px;color:var(--ink);white-space:nowrap}
.about-rule{left:531px;top:826px;width:188px;height:2px;background:var(--line)}
.body-copy{font-size:13.5px;line-height:23.7px;color:var(--text)}

/* services */
.band{left:0;top:1237px;width:1200px;height:581px;background:var(--band)}
.svc-vline{left:275px;top:1117px;width:2px;height:224px;background:var(--line)}
.svc-photo{left:592px;top:1177px;width:460px;height:329px;background:linear-gradient(110deg,#2c3440,#9aa6b3 45%,#dfe6ec 70%,#b7c3cd)}
.step-num{font-family:'Open Sans',sans-serif;font-weight:700;font-size:46px;color:var(--ink);line-height:1}
.step-title{font-family:'Open Sans',sans-serif;font-weight:600;font-size:17px;color:var(--ink);white-space:nowrap}
.step-rule{width:32px;height:2px;background:var(--line)}
.step-text{font-size:13.5px;line-height:19px;width:260px;color:var(--text)}

/* contact */
.c-label{font-family:'Open Sans',sans-serif;font-weight:600;font-size:17px;color:var(--ink)}
.c-value{font-size:17px;color:var(--ink);white-space:nowrap}
.c-social{width:26px;height:26px;border:3px solid #222;border-radius:4px}
.c-social.first{border-color:var(--nav-blue)}
.field{background:var(--field);border-radius:12px;font-size:10.5px;color:#333;padding:13px 22px}

/* newsletter & footer */
.dark{left:0;top:2342px;width:1200px;height:479px;background:var(--dark)}
.news-title{left:0;top:2398px;width:1200px;text-align:center;font-family:'Open Sans',sans-serif;font-weight:700;font-size:39px;color:var(--white)}
.news-text{left:240px;top:2458px;width:720px;text-align:center;font-size:13.5px;line-height:21px;color:#ddd;font-weight:300}
.news-input{top:2521px;height:34px;border:1px solid #666}
.f-head{top:2582px;font-family:'Open Sans',sans-serif;font-weight:600;font-size:16px;color:var(--white);white-space:nowrap}
.f-list{top:2614px;list-style:none;font-size:10px;line-height:21.7px;color:#bbb}
.f-about{left:152px;top:2614px;width:260px;font-size:10px;line-height:18.5px;color:#bbb}
.f-about a{color:var(--nav-blue);text-decoration:underline}
.f-contact{left:912px;font-size:10px;color:#bbb}
.f-contact span{position:absolute;left:22px;white-space:nowrap}
.f-divider{left:0;top:2759px;width:1200px;height:1px;background:#444}
.f-bottom{top:2775px;font-size:13px;color:#ccc;white-space:nowrap}
.f-dot{top:2773px;width:22px;height:22px;border-radius:50%;border:1.5px solid #ddd}
.f-dot.first{background:linear-gradient(90deg,var(--orange-a),var(--orange-b));border:none}
</style>
</head>
<body>

<!-- header -->
<div class="abs brand"></div>
<div class="abs brand-name">Talvora Health</div>
<div class="abs topline"></div>
<div class="abs top-social first" style="left:292px"></div>
<div class="abs top-sep" style="left:313px"></div>
<div class="abs top-social" style="left:324px"></div>
<div class="abs top-sep" style="left:345px"></div>
<div class="abs top-social" style="left:356px"></div>
<svg class="abs" style="left:781px;top:13px" width="18" height="18" viewBox="0 0 18 18"><circle cx="9" cy="9" r="7.5" fill="none" stroke="#f9a12c" stroke-width="1.6"/><path d="M9 5v4l3 2" stroke="#f9a12c" stroke-width="1.4" fill="none"/></svg>
<div class="abs top-info" style="left:809px">24/7 Clinical Team Support</div>
<div class="abs top-sep" style="left:950px"></div>
<svg class="abs" style="left:961px;top:14px" width="10" height="14" viewBox="0 0 10 14"><path d="M3 1 L5 1 L5 4 L3 5 Q3 9 5 10 L5 13 L3 13 Q0 7 3 1Z" fill="#f9a12c"/></svg>
<div class="abs top-info" style="left:978px">555-014-2290</div>
<div class="abs nav active" style="left:639px">Home</div>
<div class="abs nav" style="left:698px">About Us</div>
<div class="abs nav" style="left:772px">Services</div>
<div class="abs nav" style="left:841px">Technology</div>
<div class="abs nav" style="left:925px">Company</div>
<div class="abs nav" style="left:1000px">Contact Us</div>

<!-- hero -->
<div class="abs hero" role="img" aria-label="Oncologist in a white coat with a stethoscope, hands clasped"></div>
<div class="abs hero-kicker">Welcome To</div>
<div class="abs hero-title">Talvora Health</div>
<div class="abs hero-sub">AI software for faster, higher quality, more cost effective cancer care.</div>
<div class="btn" style="left:151px;top:381px;width:117px;height:39px;font-size:13px">Contact Us</div>

<!-- about -->
<div class="abs about-photo" role="img" aria-label="Gloved clinician preparing an oncology treatment syringe"></div>
<div class="abs ghost" style="left:613px;top:692px;font-size:72px">Who Are We</div>
<div class="abs section-title" style="left:640px;top:714px">About Us</div>
<div class="abs about-sub">Talvora Health</div>
<div class="abs about-rule"></div>
<p class="abs body-copy" style="left:640px;top:851px;width:420px">Talvora Health builds artificial intelligence software for oncology. Our platform reads clinical records, pathology and treatment history to help care teams choose evidence-based regimens sooner. For providers it means fewer delays and less paperwork; for health plans it means clearer, faster authorizations and costs that follow quality. The result is better cancer care for every patient.</p>
<div class="btn" style="left:641px;top:1005px;width:93px;height:31px;font-size:11px">Read More</div>

<!-- services -->
<div class="abs band"></div>
<div class="abs ghost" style="left:98px;top:1254px;font-size:104px;color:#e6e6e6">Services</div>
<div class="abs svc-vline"></div>
<div class="abs section-title" style="left:151px;top:1337px">Our Services</div>
<p class="abs body-copy" style="left:151px;top:1406px;width:420px">One AI platform serves both sides of oncology care. Doctors and administrators get decision support at the point of care, while payers get transparent, guideline-based review that speeds approvals and keeps treatment on the right pathway.</p>
<div class="abs svc-photo" role="img" aria-label="Team of oncologists meeting around a table with a laptop"></div>

<div class="abs step-num" style="left:149px;top:1552px">1</div>
<div class="abs step-title" style="left:150px;top:1608px">Decision Support</div>
<div class="abs step-rule" style="left:136px;top:1642px"></div>
<p class="abs step-text" style="left:150px;top:1655px">AI matches each patient to guideline and trial evidence so oncologists can choose the right regimen sooner.</p>

<div class="abs step-num" style="left:466px;top:1552px">2</div>
<div class="abs step-title" style="left:466px;top:1608px">Care Pathways</div>
<div class="abs step-rule" style="left:452px;top:1642px"></div>
<p class="abs step-text" style="left:466px;top:1655px">Practice leaders track pathway adherence, outcomes and cost across every clinic in one clear dashboard.</p>

<div class="abs step-num" style="left:782px;top:1552px">3</div>
<div class="abs step-title" style="left:782px;top:1608px">Payer Review</div>
<div class="abs step-rule" style="left:768px;top:1642px"></div>
<p class="abs step-text" style="left:782px;top:1655px">Health plans approve evidence-based cancer treatment in hours, not weeks, with automated clinical review.</p>

<!-- contact -->
<div class="abs ghost" style="left:100px;top:1830px;font-size:104px;color:#f5f5f5">Contact Us</div>
<div class="abs section-title" style="left:151px;top:1900px">Contact Us</div>
<svg class="abs" style="left:150px;top:1996px" width="16" height="30" viewBox="0 0 16 30"><path d="M5 1 L10 1 L10 7 L6 9 Q5 15 6 21 L10 23 L10 29 L5 29 Q-2 15 5 1Z" fill="#1f5fb0"/></svg>
<div class="abs c-label" style="left:197px;top:1988px">Phone:</div>
<div class="abs c-value" style="left:197px;top:2021px">555.018.4471</div>
<svg class="abs" style="left:149px;top:2084px" width="26" height="20" viewBox="0 0 26 20"><rect x="1" y="1" width="24" height="18" fill="none" stroke="#1f5fb0" stroke-width="1.8"/><path d="M1 1 L13 11 L25 1 M1 19 L10 9 M25 19 L16 9" fill="none" stroke="#1f5fb0" stroke-width="1.6"/></svg>
<div class="abs c-label" style="left:197px;top:2073px">Mail:</div>
<div class="abs c-value" style="left:199px;top:2103px">hello@talvorahealth.example</div>
<div class="abs c-social first" style="left:151px;top:2199px"></div>
<div class="abs c-social" style="left:206px;top:2199px"></div>
<div class="abs c-social" style="left:261px;top:2199px"></div>
<div class="abs c-social" style="left:314px;top:2199px"></div>

<div class="abs field" style="left:519px;top:1991px;width:253px;height:37px">Name</div>
<div class="abs field" style="left:798px;top:1991px;width:253px;height:37px">Email</div>
<div class="abs field" style="left:517px;top:2043px;width:534px;height:38px">Subject</div>
<div class="abs field" style="left:517px;top:2095px;width:534px;height:128px">Your Message</div>
<div class="btn" style="left:512px;top:2240px;width:110px;height:32px">Send</div>

<!-- newsletter -->
<div class="abs dark"></div>
<div class="abs news-title">Subscribe Our Newsletter</div>
<p class="abs news-text">Get research updates, oncology pathway news and case studies on how AI is making cancer care faster and more affordable for providers and payers alike.</p>
<div class="abs news-input" style="left:283px;width:248px"></div>
<div class="abs news-input" style="left:537px;width:248px"></div>
<div class="btn" style="left:806px;top:2521px;width:108px;height:32px">Send</div>

<!-- footer columns -->
<div class="abs f-head" style="left:152px">About Us</div>
<p class="abs f-about">Talvora Health is a medtech company using artificial intelligence to deliver higher quality, faster and more cost effective oncology care for doctors, administrators and health insurers. <a>Read More</a></p>

<div class="abs f-head" style="left:472px">Quick Links</div>
<ul class="abs f-list" style="left:472px"><li>Home</li><li>About Us</li><li>Our Platform</li><li>Our Blog</li><li>For Payers</li><li>Contact Us</li></ul>

<div class="abs f-head" style="left:716px">Quick Links</div>
<ul class="abs f-list" style="left:716px"><li>Contact Us</li><li>Terms &amp; Conditions</li><li>Privacy Policy</li><li>For Providers</li><li>Modern Slavery Act</li><li>Sitemap</li></ul>

<div class="abs f-head" style="left:912px">Contact Us</div>
<div class="abs f-contact" style="top:2614px">
  <svg width="11" height="13" viewBox="0 0 11 13"><path d="M5.5 12 Q1 7 1 5 A4.5 4.5 0 0 1 10 5 Q10 7 5.5 12Z" fill="#fff"/><circle cx="5.5" cy="5" r="1.6" fill="#151515"/></svg>
  <span style="top:0">210 Harbor Street, Suite 400</span>
  <span style="top:22px">Boston, MA 02110</span>
</div>
<div class="abs f-contact" style="top:2681px">
  <svg width="8" height="14" viewBox="0 0 8 14"><path d="M3 1 L6 1 L6 4 L4 5 Q3.5 7 4 9 L6 10 L6 13 L3 13 Q-1 7 3 1Z" fill="#fff"/></svg>
  <span style="top:0">555 019 3382</span>
</div>
<div class="abs f-contact" style="top:2725px">
  <svg width="12" height="10" viewBox="0 0 12 10"><rect x=".5" y=".5" width="11" height="9" fill="none" stroke="#fff"/><path d="M.5 .5 L6 5 L11.5 .5" fill="none" stroke="#fff"/></svg>
  <span style="top:0">care@talvorahealth.example</span>
</div>

<div class="abs f-divider"></div>
<div class="abs f-bottom" style="left:152px">All Rights Reserved &nbsp;|&nbsp; Privacy Policy</div>
<div class="abs f-dot first" style="left:554px"></div>
<div class="abs f-dot" style="left:589px"></div>
<div class="abs f-dot" style="left:624px"></div>
<div class="abs f-bottom" style="left:928px">© 2020 &nbsp;Talvora Health</div>

</body>
</html>
```